An anniversary gift for my girlfriend

My girlfriend and I have been dating for almost 2 years. We met online and this has afforded us the really unique opportunity to have the first words we said to each other (the whole conversation, in fact) preserved. We're moving in together in a few months and she doesn't know that I saved the conversation. I've been waiting for this to turn it into something we can hang in our new place.

The only phrase I want to use is:
"Well if you dislike people's knees then I think we'll get along famously"

It's an Nobody Leaves Before Midnight in Portland reference for the curious.

I want the poster to use the words themselves as the art; I'm thinking typography. I'd like it to match her aesthetic, she likes to wear Nora Vell and T. Brisk. Colors shouldn't be anything too "girly". Somewhere I'd like to include the date June 1, 2015. It shouldn't be a major piece of the poster though, just a way to denote the date.

It should fit (and be fully visible in) a 16x20 (inches) frame

Thanks in advance for the work!

Requirements
Must have
• Must use only the words: "Well if you dislike people's knees then I think we'll get along famously"
• I want this to be typography, so making the phrase the center of the poster and the art itself.

```html
<!DOCTYPE html>
<html lang="en">
<head>
<meta charset="utf-8">
<title>Well if you dislike people's knees — anniversary poster</title>
<link rel="stylesheet" href="https://fonts.googleapis.com/css2?family=Dancing+Script:wght@500&family=Oswald:wght@300&display=swap">
<style>
  :root {
    --paper: #e8e8e8;
    --skyline-dark: #bcbcbc;
    --skyline-light: #dcdcdc;
    --ink-blue: #1f78c4;
    --halo: #ffffff;
  }
  * { margin: 0; padding: 0; box-sizing: border-box; }
  html, body {
    width: 1200px;
    height: 960px;
    overflow: hidden;
    background: var(--paper);
  }
  .poster {
    position: relative;
    width: 1200px;
    height: 960px;
    background: var(--paper);
  }
  .skyline {
    position: absolute;
    left: 75px;
    top: 160px;
    width: 1050px;
    height: 383px;
  }
  .quote {
    position: absolute;
    left: 0;
    top: 352px;
    width: 1200px;
    text-align: center;
    font-family: "Dancing Script", cursive;
    font-weight: 500;
    font-size: 86px;
    line-height: 104px;
    color: var(--ink-blue);
    text-shadow:
      2px 0 0 var(--halo), -2px 0 0 var(--halo),
      0 2px 0 var(--halo), 0 -2px 0 var(--halo),
      2px 2px 0 var(--halo), -2px -2px 0 var(--halo),
      2px -2px 0 var(--halo), -2px 2px 0 var(--halo);
  }
  .quote__line { display: block; }
  .date {
    position: absolute;
    left: 0;
    top: 735px;
    width: 1200px;
    text-align: center;
    font-family: "Oswald", sans-serif;
    font-weight: 300;
    font-size: 66px;
    line-height: 80px;
    letter-spacing: -1px;
    color: var(--ink-blue);
  }
</style>
</head>
<body>
  <main class="poster">
    <svg class="skyline" viewBox="0 0 1050 383" role="img" aria-label="Grey city skyline silhouette of office towers and spires">
      <defs>
        <linearGradient id="skyline-tone" x1="0" y1="0" x2="0" y2="1">
          <stop offset="0" stop-color="var(--skyline-light)"/>
          <stop offset="0.45" stop-color="var(--skyline-dark)"/>
          <stop offset="1" stop-color="var(--skyline-dark)"/>
        </linearGradient>
      </defs>
      <rect x="0" y="0" width="1050" height="383" fill="url(#skyline-tone)"/>
    </svg>

    <h1 class="quote">
      <span class="quote__line">Well if you dislike people’s knees</span>
      <span class="quote__line">then I think we’ll get</span>
      <span class="quote__line">along famously.</span>
    </h1>

    <p class="date">June 1, 2015</p>
  </main>
</body>
</html>
```